Card design for orthopaedic surgeons working as The Meridale Orthopaedic Clinic

Business cards, letterhead

Colors

Designer to choose colors to be used in the design.

Requirements
Must have
• Late addition.
• Cards letterhead must have logos of
• Corvane Federated Guild of Surgeons
• Tellmark Orthopaedic Society
Nice to have
• Back of card to have space for appointment time to be added by hand and some blank space for writing incidental other notes.

```html
<!DOCTYPE html>
<html lang="en">
<head>
<meta charset="utf-8">
<title>The Meridale Orthopaedic Clinic — Business Card</title>
<link href="https://fonts.googleapis.com/css2?family=Montserrat:wght@400&family=Open+Sans:wght@400;600;700&display=swap" rel="stylesheet">
<style>
  :root {
    --backdrop: #d9dadc;
    --card: #ffffff;
    --brand-blue: #3aa9ea;
    --ink-navy: #1f3352;
    --card-shadow: rgba(0, 0, 0, 0.18);
  }
  * { box-sizing: border-box; margin: 0; padding: 0; }
  html, body {
    width: 1200px;
    height: 800px;
    overflow: hidden;
  }
  body {
    background: var(--backdrop);
    font-family: "Open Sans", Arial, sans-serif;
    color: var(--ink-navy);
    position: relative;
  }
  .card {
    position: absolute;
    width: 490px;
    height: 280px;
    background: var(--card);
    box-shadow: 0 6px 18px var(--card-shadow);
  }
  .brand-name {
    font-family: "Montserrat", Arial, sans-serif;
    font-weight: 400;
    color: var(--brand-blue);
    white-space: nowrap;
    letter-spacing: -0.3px;
  }

  /* Front */
  .card-front {
    left: 60px;
    top: 260px;
    text-align: center;
  }
  .card-front .brand-name {
    margin-top: 112px;
    font-size: 25px;
    line-height: 1.2;
  }
  .card-front .web-line {
    margin-top: 22px;
    font-size: 13px;
  }

  /* Back */
  .card-back {
    left: 650px;
    top: 260px;
  }
  .card-back .brand-name {
    position: absolute;
    left: 32px;
    top: 52px;
    font-size: 17px;
    line-height: 1.2;
  }
  .holder {
    position: absolute;
    right: 40px;
    top: 160px;
    text-align: right;
  }
  .holder-name {
    font-size: 24px;
    font-weight: 700;
    color: var(--brand-blue);
    line-height: 1.1;
  }
  .holder-role {
    font-size: 12.5px;
    line-height: 1.4;
  }
  .divider {
    position: absolute;
    left: 40px;
    right: 40px;
    top: 215px;
    height: 4px;
    background: var(--brand-blue);
  }
  .contact {
    position: absolute;
    left: 0;
    right: 0;
    top: 228px;
    text-align: center;
    font-size: 12.5px;
    line-height: 1.5;
    white-space: nowrap;
  }
  .contact .icon-mail {
    display: inline-block;
    vertical-align: -1px;
    margin: 0 4px;
  }
</style>
</head>
<body>

  <section class="card card-front" aria-label="Business card front">
    <p class="brand-name">The Meridale Orthopaedic Clinic</p>
    <p class="web-line">Web : xxxxxxxxxxxxxxxxx</p>
  </section>

  <section class="card card-back" aria-label="Business card back">
    <p class="brand-name">The Meridale Orthopaedic Clinic</p>
    <div class="holder">
      <p class="holder-name">NAME</p>
      <p class="holder-role">Designation</p>
    </div>
    <div class="divider"></div>
    <div class="contact">
      <p>Address xxxxxxxxxxxxxxxxxxxxxxxxxxxxxxxxxxxxxxx</p>
      <p>Mobile xxxxxxxxxxx
        <svg class="icon-mail" width="11" height="11" viewBox="0 0 11 11" aria-hidden="true">
          <circle cx="5.5" cy="5.5" r="5.5" fill="var(--brand-blue)"/>
          <rect x="2.6" y="3.6" width="5.8" height="3.8" fill="none" stroke="#fff" stroke-width="0.8"/>
          <path d="M2.6 3.6 L5.5 5.8 L8.4 3.6" fill="none" stroke="#fff" stroke-width="0.8"/>
        </svg>
        Email ID xxxxxxxxxxxxxxxxxxx</p>
    </div>
  </section>

</body>
</html>
```